Menu Design, lay out and font to be professionally finished

We need a menu designed.

We need to have a similar font that is used in our logo. It is an old type writer font, we also have some flecks in it to make it look old. We would like this to be consistant throughout the menu.

We would need it to be formatted very professionally. We would like our logo used in the title of the menu.

The menu will be on A4 paper.

It would be preferable if the menu could be on a word document so it can be altered easily, Im not sure if we can get the required font through word?

We will require the winning designer to also complete a simple drinks menu in the same style as the food menu. This is included in the the project.

Requirements
Must have
• I just need the font to look like it was typed on an old type writer? I will print on old looking paper!

```html
<!DOCTYPE html>
<html lang="en">
<head>
<meta charset="utf-8">
<title>the Fox &amp; Heron – All Day Menu</title>
<link rel="stylesheet" href="https://fonts.googleapis.com/css2?family=Special+Elite&display=swap">
<style>
  :root {
    --wood-dark: #8a5a32;
    --wood-mid: #b07a45;
    --wood-light: #c9955e;
    --paper: #fbfaf6;
    --rule-blue: #a9c6e2;
    --margin-red: #e59a9a;
    --ink: #2b2622;
    --title-ink: #f6efe4;
    --highlight: #f6f06a;
    --hole: #6e4527;
    --pin: #b9b9b9;
    --pin-edge: #7d7d7d;
  }
  * { margin: 0; padding: 0; box-sizing: border-box; }
  html, body { width: 849px; height: 1200px; overflow: hidden; }
  body { font-family: 'Special Elite', 'Courier New', monospace; color: var(--ink); }

  .menu-board {
    position: relative;
    width: 849px; height: 1200px;
    background: linear-gradient(90deg, var(--wood-dark), var(--wood-mid) 30%, var(--wood-light) 55%, var(--wood-mid) 80%, var(--wood-dark));
  }

  .title {
    position: absolute; left: 150px; top: 38px;
    color: var(--title-ink); font-size: 44px; font-weight: 400; line-height: 1; letter-spacing: 1px;
  }
  .subtitle {
    position: absolute; right: 48px; top: 82px;
    color: var(--title-ink); font-size: 26px;
  }

  .notepad {
    position: absolute; left: 52px; top: 135px; width: 746px; height: 1040px;
    background-color: var(--paper);
    background-image:
      linear-gradient(90deg, transparent 72px, var(--margin-red) 72px, var(--margin-red) 74px, transparent 74px),
      repeating-linear-gradient(180deg, transparent 0, transparent 19px, var(--rule-blue) 19px, var(--rule-blue) 20px);
    background-position: 0 0, 0 36px;
    background-repeat: no-repeat, repeat;
    background-size: 100% 100%, 100% 20px;
    box-shadow: 2px 4px 10px rgba(0,0,0,.35);
  }
  .notepad .spiral { position: absolute; left: 0; top: 10px; }

  .pin { position: absolute; }

  .item {
    position: absolute; left: 100px; width: 610px;
    font-size: 14px; line-height: 20px;
  }
  .item .name { display: block; width: 540px; }
  .item .price { position: absolute; right: 0; top: 0; }
  .item .price.second { top: 20px; }
  .mark { background: var(--highlight); }
</style>
</head>
<body>
<main class="menu-board">
  <h1 class="title">the Fox &amp; Heron</h1>
  <p class="subtitle">All Day Menu</p>

  <section class="notepad">
    <svg class="spiral" width="746" height="16" viewBox="0 0 746 16" aria-hidden="true">
      <g fill="var(--hole)">
        <circle cx="28" cy="8" r="4"/><circle cx="56" cy="8" r="4"/><circle cx="84" cy="8" r="4"/><circle cx="112" cy="8" r="4"/><circle cx="140" cy="8" r="4"/><circle cx="168" cy="8" r="4"/><circle cx="196" cy="8" r="4"/><circle cx="224" cy="8" r="4"/><circle cx="252" cy="8" r="4"/><circle cx="280" cy="8" r="4"/><circle cx="308" cy="8" r="4"/><circle cx="336" cy="8" r="4"/><circle cx="364" cy="8" r="4"/><circle cx="392" cy="8" r="4"/><circle cx="420" cy="8" r="4"/><circle cx="448" cy="8" r="4"/><circle cx="476" cy="8" r="4"/><circle cx="504" cy="8" r="4"/><circle cx="532" cy="8" r="4"/><circle cx="560" cy="8" r="4"/><circle cx="588" cy="8" r="4"/><circle cx="616" cy="8" r="4"/><circle cx="644" cy="8" r="4"/><circle cx="672" cy="8" r="4"/><circle cx="700" cy="8" r="4"/><circle cx="728" cy="8" r="4"/>
      </g>
    </svg>

    <p class="item intro" style="top:57px"><span class="mark">At The Fox &amp; Heron all our eggs are organic.<br>Our meat is free range &amp; organic where possible.<br>Breads are sourdough, baked daily by Ollie.<br>See front counter for daily sweet selection.</span></p>

    <p class="item" style="top:168px"><span class="name">Ollie's toasted sourdough with house made butter &amp; spreads<br>(Gluten free also available)</span><span class="price second">$6</span></p>
    <p class="item" style="top:230px"><span class="name">Our granola with Earl Grey figs, yogurt &amp; Granny Smith slaw</span><span class="price">$10</span></p>
    <p class="item" style="top:270px"><span class="name">Buckwheat and quinoa porridge with poached red fruits and coconut caramel</span><span class="price">$10</span></p>
    <p class="item" style="top:346px"><span class="name">Two poached eggs on sourdough with smoked tomato relish</span><span class="price">$10</span></p>
    <p class="item" style="top:388px"><span class="name">Sides: Roast tomato, field mushroom, avocado, feta<br>&nbsp;&nbsp;&nbsp;&nbsp;&nbsp;&nbsp;Bacon, pork sausage, smoked salmon</span><span class="price">$4</span><span class="price second">$6</span></p>
    <p class="item" style="top:456px"><span class="name">Bacon and egg roll – two fried organic eggs, bacon, caramelized onion, slaw &amp; espresso bbq sauce</span><span class="price">$10</span></p>
    <p class="item" style="top:527px"><span class="name">Smashed avocado on toast with broad beans, mint and feta</span><span class="price">$15</span></p>
    <p class="item" style="top:572px"><span class="name">Smoked trout salmon on toast with house made labne, pickled fennel and roe</span><span class="price">$15</span></p>
    <p class="item" style="top:635px"><span class="name">Kellan Creek steak sandwich with burnt onions, smoked mozzarella, lettuce, tomato, <span class="mark">$15 pickles &amp; mayo</span></span></p>
    <p class="item" style="top:731px"><span class="name">Salad of asparagus, broad beans &amp; zucchini with green wheat &amp; sesame yogurt</span><span class="price">$16.5</span></p>
    <p class="item" style="top:793px"><span class="name">Heron's Big Breakfast<br>Pork sausage, bacon, fried eggs, roast tomato, field mushrooms &amp; Boston beans with sourdough toast</span><span class="price">$19</span></p>
    <p class="item" style="top:870px"><span class="name">Bowl of sweet potato chips with pink river salt &amp; aioli</span><span class="price">$8</span></p>
    <p class="item" style="top:915px"><span class="name">Kids Meal<br>Little sausage sandwich plus a treat for later if they eat their peas</span><span class="price second">$8</span></p>
    <p class="item" style="top:980px"><span class="name">Seasonal fruit cup with hazelnut spread for dipping</span><span class="price">$5</span></p>
  </section>

  <svg class="pin" style="left:40px;top:140px" width="22" height="22" aria-hidden="true"><circle cx="11" cy="11" r="8" fill="var(--pin)" stroke="var(--pin-edge)" stroke-width="2"/><path d="M5 11h12M11 5v12" stroke="var(--pin-edge)" stroke-width="1.5"/></svg>
  <svg class="pin" style="left:787px;top:140px" width="22" height="22" aria-hidden="true"><circle cx="11" cy="11" r="8" fill="var(--pin)" stroke="var(--pin-edge)" stroke-width="2"/><path d="M5 11h12M11 5v12" stroke="var(--pin-edge)" stroke-width="1.5"/></svg>
  <svg class="pin" style="left:40px;top:1155px" width="22" height="22" aria-hidden="true"><circle cx="11" cy="11" r="8" fill="var(--pin)" stroke="var(--pin-edge)" stroke-width="2"/><path d="M5 11h12M11 5v12" stroke="var(--pin-edge)" stroke-width="1.5"/></svg>
  <svg class="pin" style="left:787px;top:1155px" width="22" height="22" aria-hidden="true"><circle cx="11" cy="11" r="8" fill="var(--pin)" stroke="var(--pin-edge)" stroke-width="2"/><path d="M5 11h12M11 5v12" stroke="var(--pin-edge)" stroke-width="1.5"/></svg>
</main>
</body>
</html>
```